Lumeno-Interior design firm
Hello all,
I will announce the winner in the next few hours...
I appreciate your AMAZING ideas and all the many revisions that each of you submited, they helped us to understand your creative proposals and at the end to select a winner.
THANK YOU!
Lumeno Design
Draft #317 and #318
We are looking at some winning designs already and we will send our efforts towards those. i appreciate your entry very much.
Thanks!
Draft #312
The font on the subject LUMENO Interior design firm needs to be changed. I dont like it. I like the font used on the HOME, PORTFOLIO, etc...main subjects if that helps!
Everything else looks amazing!
hi all,
I had an unexpected business to attend today and I was not able to complete the feedback to all of you. We decided to extend the time to provide the missing feedback...I will provide to all, just give me some time.
I have decided to extend the contest. This was a last minute descision.
I appreciate your entry but is not what I am looking for. I don't want to waste your time as well as I prefer to concentrate on the designs/designers that have invested some time with me already.
Thank you and I appreciate your understanding!
Thanks brightquill! I really appreciate your understanding!
Draft #273
Can you justified all the texts used on each page? That will be great for final review.
Drafts #270 and #272
the text needs to be justified and that will make it!
Draft #269
HOME
There is a small misspell at the bottom left...it reads Lemeno instead of Lumeno.
Ater that revision you are set!
@PH, Thanks for your comments...
Dear Brightquill,
I like your entry but i am sorry to say that there is nothing original about it. I feel respect for everyones work and even when I am not an expert I feel you are copying other entries. I can not give you credit for someone else's ideas and I would appreciate if you come up with the same concept but with something that is your very own creation.
With all my respect...
Draft #251
Looks good just to revise the "yellow" cubes to be softer...and also please use my pictures for each page so I can compare with everyone else.
Thank you so much!
Draft #250
I would prefer to container the ABOUT US description on within the limits of the cubes so if necessary lets remove the "yellow" cubes so we can move up the wording and fit it within...
Use the service wording as reference...it is contained and it does not go below the "cubes"
Draft #249
lets list the services on a horizontal way inside the "cubes" Makes sense? linear way showing the services and the main wording as is.
Draft #248
can we made the windows with tabs LIVING, DINING, BEDROOM ACCENTS and KIDS to be one of the "cubes" from your design?
maybe using the bottom five...?
then when you click on I would like to see a complete picture...hopefully you come up with an idea but if not we can look at it together after revision...
Thanks
Draft #247
My only change is the "yellow" buttons to be more with softer colors...soft grey/white...or any suggestions within my request.
Draft #234
Wording needs to be consistent...I prefer white please revise.
Draft #227
Revisions:
I dont like the phone image under phone, please remove
Please do not underline the website
I prefer just letter on the front:
P: for phone
W: for website
etc...
In your case I would prefer not to use my picture...lets just remove it and after all this it should be done!
Looking good!
Draft #223
I need you to add the wording that I sent for services as well...it is important!
Thanks! Everything else looks perfect!
Hello@PH
I`m just waiting for your Feedback on
#221(Home page), #222(Portfolio Page), #223(Services Page),#224(About Us Page), & #225(Contact Page)
Zora
FOR EVERYONE:
PLEASE submit your complete designs, I wont be extending the project and with the time left I wont be able to give feedback and revisions to detail to everyone.
I really appreciate your hard work on attention to my project.
You ALL are very talented!
Good luck!
Draft #208 you can move forward with the inner pages.
Draft #207
I need the text to be justified please. You can complete your design with all he pages, I like the layout as is.
Look forward to final entries.

```html
<!DOCTYPE html>
<html lang="en">
<head>
<meta charset="utf-8">
<title>Lumeno – Interior Design, Architecture, Art</title>
<link href="https://fonts.googleapis.com/css2?family=Questrial&family=Arimo:wght@400;700&display=swap" rel="stylesheet">
<style>
  :root {
    --bg: #e6e5e0;
    --bg-light: #efeee9;
    --gold: #b59a52;
    --gold-soft: #c6b27a;
    --frame: #ffffff;
    --nav-text: #ffffff;
    --nav-muted: #b9aaa0;
    --footer-text: #8f8d87;
    --icon: #9a9891;
  }
  * { box-sizing: border-box; margin: 0; padding: 0; }
  html, body { width: 1200px; height: 901px; overflow: hidden; }
  body {
    position: relative;
    background: var(--bg);
    font-family: "Arimo", Arial, sans-serif;
  }
  .backdrop-art {
    position: absolute;
    left: 760px; top: 0;
    width: 440px; height: 901px;
    background: linear-gradient(100deg, var(--bg) 0%, var(--bg-light) 45%, var(--bg) 100%);
  }
  .brand {
    position: absolute;
    left: 200px; top: 52px;
    display: flex; align-items: center; gap: 26px;
  }
  .brand-mark {
    width: 22px; height: 22px;
    background: var(--gold);
  }
  .brand-name {
    font-family: "Questrial", sans-serif;
    font-size: 62px;
    letter-spacing: 6px;
    color: var(--gold-soft);
    line-height: 1;
  }
  .brand-tagline {
    font-family: "Questrial", sans-serif;
    font-size: 16.5px;
    color: var(--gold);
    margin-top: 6px;
    letter-spacing: 0.3px;
  }
  .showcase {
    position: absolute;
    left: 200px; top: 187px;
    width: 798px; height: 502px;
    background: var(--frame);
    padding: 6px;
    box-shadow: 0 2px 8px rgba(0,0,0,0.25);
  }
  .showcase-photo {
    width: 100%; height: 100%;
    background:
      linear-gradient(180deg, #cfd6c4 0%, #7f9366 22%, #8b6a4a 38%, #6b2a1f 58%, #4a1d14 78%, #2e1410 100%);
  }
  .main-nav {
    position: absolute;
    right: 235px; top: 541px;
    list-style: none;
    text-align: right;
  }
  .main-nav li {
    font-size: 18px;
    line-height: 35.5px;
    color: var(--nav-text);
    text-transform: uppercase;
  }
  .main-nav li.is-current { color: var(--nav-muted); }
  .rooms {
    position: absolute;
    left: 200px; top: 713px;
    display: flex; gap: 17px;
  }
  .room {
    position: relative;
    width: 105px; height: 66px;
    background: var(--frame);
    padding: 3px;
    box-shadow: 0 1px 4px rgba(0,0,0,0.3);
  }
  .room-photo { width: 100%; height: 100%; }
  .room-label {
    position: absolute;
    left: 0; right: 0; bottom: 6px;
    text-align: center;
    font-size: 10px;
    color: var(--nav-text);
  }
  .room--living .room-photo  { background: linear-gradient(180deg, #a9a27e, #6b3a26 60%, #3b1d14); }
  .room--dining .room-photo  { background: linear-gradient(180deg, #c2c4b2, #7f7154 55%, #4a3a2a); }
  .room--bedroom .room-photo { background: linear-gradient(180deg, #d6d1c6, #8f857a 55%, #3e3630); }
  .room--accent .room-photo  { background: linear-gradient(180deg, #9b8f6a, #7a5a33 55%, #4a3320); }
  .room--kids .room-photo    { background: linear-gradient(180deg, #ece8e0, #c9c3b8 55%, #a39b90); }
  .site-footer {
    position: absolute;
    left: 200px; right: 202px; top: 872px;
    display: flex; justify-content: space-between; align-items: center;
    font-size: 11.5px;
    color: var(--footer-text);
  }
  .social { display: flex; align-items: center; gap: 8px; }
  .social-label { margin-right: 6px; }
  .social-dot { width: 24px; height: 24px; background: var(--icon); border-radius: 3px; }
</style>
</head>
<body>
  <div class="backdrop-art" role="img" aria-label="Faint decorative branches on the background"></div>

  <header class="brand">
    <span class="brand-mark"></span>
    <div>
      <div class="brand-name">LUMENO</div>
      <div class="brand-tagline">Interior Design • Architecture • Art</div>
    </div>
  </header>

  <main class="showcase">
    <div class="showcase-photo" role="img" aria-label="Living room with red sectional sofa, wooden coffee table and garden view"></div>
  </main>

  <ul class="main-nav">
    <li>Home</li>
    <li class="is-current">Portfolio</li>
    <li>About Us</li>
    <li>Contact</li>
  </ul>

  <nav class="rooms">
    <div class="room room--living"><div class="room-photo" role="img" aria-label="Living room"></div><span class="room-label">LIVING</span></div>
    <div class="room room--dining"><div class="room-photo" role="img" aria-label="Dining room"></div><span class="room-label">DINING</span></div>
    <div class="room room--bedroom"><div class="room-photo" role="img" aria-label="Bedroom"></div><span class="room-label">BEDROOM</span></div>
    <div class="room room--accent"><div class="room-photo" role="img" aria-label="Accent decor"></div><span class="room-label">ACCENT</span></div>
    <div class="room room--kids"><div class="room-photo" role="img" aria-label="Kids room"></div><span class="room-label">KIDS</span></div>
  </nav>

  <footer class="site-footer">
    <p>Copyright&nbsp; 2011, All Rights Reserved.&nbsp; LUMENO | Interior Design, Architecture, Art</p>
    <div class="social">
      <span class="social-label">Follow Us On:</span>
      <span class="social-dot"></span>
      <span class="social-dot"></span>
    </div>
  </footer>
</body>
</html>
```